Business card for a plastic surgeon

i need a business card for a plastic surgeon. I have two adresses. The card should communicate safety, simmetry, beauty and with soft colors.
What i want in the card:
- my logo: Letters "R"and "B" (picture uploaded)
- my name: Renato Bastiani
- my registration: CRM 507 219
- my adresses and phone numbers (2):
- Av Dr Teixeira Lopes, 2710, sala 305 - Vila Olímpia | São Paulo/ SP - Phone: 11 4172-5036
- Al. Itapeva, 47, 3 andar - Alphaville | Barueri/ SP - Phone: 11 6350-2481

- my social network: site, facebook and instagram

Target Market(s)

people (95% girls and women) that want cosmetic procedures and plastic surgery

Industry/Entity Type

Business

Contact Information for Business Card

The card should communicate safety, simmetry, beauty and with soft colors.
Beige, brown, gray, rosy are some options. Color is free

Font styles to use
Serif

Requirements
Must have
• - my logo: Letters "R"and "B" (picture uploaded)
• - my name: Renato Bastiani
• - my registration: CRM 507 219
• - my adresses and phone numbers (2):
• - Av Dr Teixeira Lopes, 2710, sala 305 - Vila Olímpia | São Paulo/ SP - Phone: 11 4172-5036
• - Al. Itapeva, 47, 3 andar - Alphaville | Barueri/ SP - Phone: 11 6350-2481
• - my social network: site, facebook and instagram
Should not have
• other images (only my logo)

```html
<!DOCTYPE html>
<html lang="pt-BR">
<head>
<meta charset="UTF-8">
<title>Renato Bastiani · Cirurgião Plástico · Cartão de visita</title>
<link rel="stylesheet" href="https://fonts.googleapis.com/css2?family=Cinzel:wght@400;500&family=Roboto:wght@300;400&display=swap">
<style>
  :root {
    --rose: #e0577f;
    --rose-deep: #c9466e;
    --rose-light: #ec6f92;
    --ink: #1e1e1e;
    --text: #4a4a4a;
    --rule: #3a3a3a;
    --paper: #f7f7f7;
    --backdrop: #ece8e4;
  }
  * { box-sizing: border-box; margin: 0; padding: 0; }
  html, body { width: 1200px; height: 1200px; overflow: hidden; }
  body { background: var(--backdrop); position: relative; font-family: "Roboto", Arial, sans-serif; }

  .card { position: absolute; width: 733px; height: 418px; box-shadow: 0 6px 16px rgba(0,0,0,.18); overflow: hidden; }

  /* Front */
  .card-front { left: 132px; top: 167px; background: linear-gradient(120deg, #fff 0%, var(--paper) 40%, #fff 60%, #f1f1f1 100%); border-radius: 0 34px 0 34px; }
  .brand-mark { position: absolute; left: 0; right: 0; top: 92px; text-align: center; font-family: "Cinzel", Georgia, serif; font-size: 26px; color: var(--ink); letter-spacing: 1px; }
  .doctor-name { position: absolute; left: 0; right: 0; top: 156px; text-align: center; font-family: "Cinzel", Georgia, serif; font-size: 24px; color: var(--ink); letter-spacing: .5px; }
  .specialty { position: absolute; left: 0; right: 0; top: 184px; text-align: center; font-family: "Cinzel", Georgia, serif; font-size: 11.5px; letter-spacing: 3.4px; color: var(--ink); }
  .registration { position: absolute; left: 246px; width: 242px; top: 201px; display: flex; align-items: center; gap: 6px; font-family: "Cinzel", Georgia, serif; font-size: 11px; letter-spacing: 1px; color: var(--ink); }
  .registration::before, .registration::after { content: ""; flex: 1; height: 1px; background: var(--rule); }

  .contact { position: absolute; top: 256px; font-size: 16px; color: var(--text); line-height: 23px; }
  .contact-left { left: 38px; }
  .contact-right { right: 32px; text-align: right; }
  .contact-row { display: flex; align-items: center; gap: 9px; }
  .contact-right .contact-row { justify-content: flex-end; }
  .contact .phone { letter-spacing: 1.6px; }
  .contact .city-left { letter-spacing: 1.4px; padding-left: 24px; }
  .contact .city-right { font-size: 15px; letter-spacing: -.3px; padding-right: 22px; }
  .icon { width: 15px; height: 15px; fill: var(--rose); flex: none; }

  .divider { position: absolute; left: 36px; right: 30px; top: 332px; height: 1px; background: var(--rule); }
  .social { position: absolute; top: 346px; display: flex; align-items: center; gap: 12px; font-size: 16px; color: var(--text); }
  .social-left { left: 38px; }
  .social-right { right: 34px; }
  .social-square { width: 28px; height: 28px; border-radius: 4px; background: var(--rose); }

  .band-thin { position: absolute; left: 0; right: 0; top: 389px; height: 3px; background: var(--rose); }
  .band-thick { position: absolute; left: 0; right: 0; top: 398px; height: 20px; background: var(--rose); }

  /* Back */
  .card-back { left: 320px; top: 637px; border-radius: 34px 0 34px 0; background: linear-gradient(120deg, var(--rose-deep) 0%, var(--rose-light) 30%, var(--rose-deep) 50%, var(--rose) 65%, var(--rose-light) 100%); display: flex; align-items: center; justify-content: center; }
  .back-mark { font-family: "Cinzel", Georgia, serif; font-size: 34px; color: #fff; letter-spacing: 2px; }
</style>
</head>
<body>
  <section class="card card-front" aria-label="Frente do cartão">
    <div class="brand-mark">Renato Bastiani</div>
    <h1 class="doctor-name">DR. RENATO BASTIANI</h1>
    <p class="specialty">CIRURGIÃO PLÁSTICO</p>
    <p class="registration">CRM 507 219</p>

    <div class="contact contact-left">
      <div class="contact-row">
        <svg class="icon" viewBox="0 0 16 16"><path d="M1 6c0-2 3-4 7-4s7 2 7 4v1h-3V5.5H4V7H1z M3 8h10l1 6H2z"/></svg>
        <span class="phone">11 6350-2481</span>
      </div>
      <div class="contact-row">
        <svg class="icon" viewBox="0 0 16 16"><path d="M8 1l7 7h-2v7H10v-5H6v5H3V8H1z"/></svg>
        <span>Al. Itapeva, 47, 3 andar</span>
      </div>
      <div class="contact-row"><span class="city-left">Alphaville | Barueri/ SP</span></div>
    </div>

    <div class="contact contact-right">
      <div class="contact-row">
        <span class="phone">11 4172-5036</span>
        <svg class="icon" viewBox="0 0 16 16"><path d="M1 6c0-2 3-4 7-4s7 2 7 4v1h-3V5.5H4V7H1z M3 8h10l1 6H2z"/></svg>
      </div>
      <div class="contact-row">
        <span>Av Dr Teixeira Lopes, 2710</span>
        <svg class="icon" viewBox="0 0 16 16"><path d="M8 1l7 7h-2v7H10v-5H6v5H3V8H1z"/></svg>
      </div>
      <div class="contact-row"><span class="city-right">sala 305 - Vila Olímpia | São Paulo/ SP</span></div>
    </div>

    <div class="divider"></div>
    <div class="social social-left"><span class="social-square"></span><span>Renato Bastiani</span></div>
    <div class="social social-right"><span>Renato Bastiani</span><span class="social-square"></span></div>

    <div class="band-thin"></div>
    <div class="band-thick"></div>
  </section>

  <section class="card card-back" aria-label="Verso do cartão">
    <div class="back-mark">Renato Bastiani</div>
  </section>
</body>
</html>
```